3D Scans and Virtual Tour photography company needs a website

We need a website build that explains what we do, shows some examples of our 3d scans and virtual tours, some stats on why they are important when when selling your home or marketing your business/premises and a contact form to find out more. We need to target both the real estate agents and consumers. The site needs to looks modern, engaging, clean, not lots of text but more pictures and icons. Needs to be mobile friendly. In fact i would build it from the mobile then out.
Updates

Project Deadline Extended
Reason: Hi Team, I have had a couple of requests to extend the Project deadline, which I have now done. I cant push it much more than this as the business is up and running now and I need the website. Looking forward to reviewing the designs.

Target Market(s)

people selling their home and the real estate industry mostly, however any building can be scanned and have a 3d tour

Industry/Entity Type

Photographer

Font styles to use
Sans Serif

Colors
32a6d6
0355a3
33a6d7
85cae6
cee9f5
3176b5

Requirements
Must have
• Our logo
• an example of the 3d scans
• an example of a dollhouse view
• a contact page
• Replace the orange document examples to blue please
• social media links Quillnest Pondlarken Zembol
Nice to have
• some examples of similar companies websites we like
• favourite would be this one hollanbrick (dot com)
• next fav orvantile (dot com au) and brevolux (dot com au)

```html
<!DOCTYPE html>
<html lang="en">
<head>
<meta charset="utf-8">
<title>Brightvale Imagery — 3D Scans &amp; Virtual Tours</title>
<link rel="stylesheet" href="https://fonts.googleapis.com/css2?family=Montserrat:wght@400;500;600;700&family=Open+Sans:wght@400;600;700&display=swap">
<style>
:root{
  --sky:#32a6d6;
  --navy:#0355a3;
  --deep:#0f47a0;
  --band:#2f90d8;
  --pale:#85cae6;
  --mist:#cee9f5;
  --mid:#3176b5;
  --grey:#e6e6e6;
  --ink:#222;
  --soft:#666;
  --white:#fff;
}
*{box-sizing:border-box;margin:0;padding:0}
html,body{width:1200px;height:5325px;overflow:hidden}
body{font-family:"Open Sans",Arial,sans-serif;color:var(--ink);background:var(--white);position:relative}
h1,h2,h3,h4,.nav,.btn{font-family:"Montserrat",Arial,sans-serif}
section,header,footer{position:absolute;left:0;width:1200px}
.abs{position:absolute}
.btn{display:inline-block;background:var(--navy);color:var(--white);font-size:13px;font-weight:600;border-radius:16px;padding:9px 22px}

/* header */
.site-header{top:0;height:100px;background:var(--white)}
.brand{left:132px;top:24px;font-family:"Montserrat",Arial,sans-serif;font-weight:700;font-size:26px;color:var(--mid);letter-spacing:1px}
.brand small{display:block;font-size:13px;font-weight:700;letter-spacing:7px;margin-top:-2px}
.nav{left:440px;top:52px;display:flex;gap:42px;font-size:12px;font-weight:500;color:#333}
.social{display:flex;gap:8px}
.social span{width:24px;height:24px;border-radius:50%;background:var(--mid);color:var(--white);font-size:11px;font-weight:700;display:flex;align-items:center;justify-content:center;font-family:"Montserrat",Arial,sans-serif}
.header-social{left:962px;top:44px}

/* hero */
.hero{top:100px;height:603px;background:linear-gradient(180deg,#6f8fb0 0%,#9fb3c6 40%,#7d8d72 75%,#4d6b3a 100%)}
.play{left:545px;top:216px}
.hero h1{top:365px;width:1200px;text-align:center;color:var(--white);font-size:42px;font-weight:700;line-height:54px;letter-spacing:1px}
.hero .watch{left:522px;top:512px;background:var(--sky);color:var(--white);font-size:14px;font-weight:600;padding:12px 24px;border-radius:2px;font-family:"Montserrat",Arial,sans-serif}

/* services grid */
.services{top:703px;height:529px}
.tile{position:absolute;width:600px;height:265px;color:var(--white);text-align:center;padding:80px 90px 0}
.tile h2{font-size:30px;font-weight:600;margin-bottom:8px}
.tile p{font-size:11.5px;line-height:17px;color:var(--mist)}
.t1{left:0;top:0;background:linear-gradient(135deg,#1d5fc4,#2f86e0)}
.t2{left:600px;top:0;background:linear-gradient(135deg,#2a7ee0,#1456bb)}
.t3{left:0;top:265px;background:linear-gradient(135deg,#1850b0,#2d7bd8)}
.t4{left:600px;top:265px;background:linear-gradient(135deg,#3a8de4,#1a5ec2)}

/* process */
.process{top:1232px;height:532px;background:var(--band);color:var(--white)}
.process h2{top:62px;width:1200px;text-align:center;font-size:24px;font-weight:500;letter-spacing:1px}
.process .line{left:263px;top:303px;width:660px;height:4px;background:var(--white)}
.step{position:absolute;top:164px;width:240px;margin-left:-120px;text-align:center}
.step h4{font-size:17px;font-weight:400;margin-bottom:40px;font-family:"Open Sans",Arial,sans-serif}
.step .disc{width:142px;height:142px;border-radius:50%;background:var(--white);margin:0 auto 28px;display:flex;align-items:center;justify-content:center}
.step p{font-size:13px;line-height:18px;color:var(--mist)}
.step p b{color:var(--white)}

/* feature rows */
.feature{height:436px}
.feature h2{font-size:30px;font-weight:500;line-height:42px;color:#111}
.feature h2 em{font-style:normal;color:var(--navy)}
.feature p{font-size:12px;line-height:21px;color:var(--soft)}
.tablet{position:absolute;background:#1e1e1e;border-radius:20px;padding:24px 34px}
.tablet .screen{width:100%;height:100%}
.f1{top:1764px;background:var(--white)}
.f2{top:2200px;height:430px;background:var(--grey)}
.f3{top:2630px;height:458px;background:var(--white)}

/* benefits */
.benefits{top:3088px;height:515px;background:var(--grey)}
.benefits h2{top:60px;width:1200px;text-align:center;color:var(--sky);font-size:24px;font-weight:600}
.benefits .line{left:220px;top:229px;width:778px;height:4px;background:var(--white)}
.benefit{position:absolute;top:167px;width:230px;margin-left:-115px;text-align:center}
.benefit .disc{width:128px;height:128px;border-radius:50%;background:var(--white);margin:0 auto 52px;display:flex;align-items:center;justify-content:center}
.benefit h4{color:var(--navy);font-size:13px;font-weight:600;margin-bottom:10px}
.benefit p{font-size:11.5px;line-height:19px;color:#444}
.benefit p b{color:var(--navy);font-weight:600}

/* freebies */
.freebies{top:3603px;height:560px;background:var(--white)}
.freebies .photo{left:43px;top:61px;width:514px;height:447px;background:linear-gradient(160deg,#5b6d86 0%,#9a8676 50%,#4a3b33 100%)}
.freebies .panel{left:557px;top:61px;width:597px;height:447px;background:var(--navy);color:var(--white);padding:46px 52px}
.panel h2{font-size:24px;font-weight:600;margin-bottom:34px;letter-spacing:1px}
.panel li{list-style:none;display:flex;align-items:center;gap:26px;height:63px;font-size:13px;color:var(--mist)}

/* feed */
.feed{top:4163px;height:317px;background:var(--white)}
.feed h2{top:33px;width:1200px;text-align:center;color:var(--sky);font-size:26px;font-weight:600}
.post{position:absolute;top:151px;width:300px;display:flex;gap:16px}
.post .thumb{width:40px;height:40px;background:linear-gradient(135deg,#88a0b8,#c9b9a4);flex:none}
.post h4{font-size:13px;color:var(--navy);font-weight:600;line-height:17px;font-family:"Open Sans",Arial,sans-serif}
.post p{font-size:11px;color:var(--soft);margin-top:8px}
.post + .divider{}
.divider{position:absolute;top:140px;width:1px;height:80px;background:#ddd}

/* contact */
.contact{top:4480px;height:632px;background:var(--deep)}
.contact h2{top:68px;width:1200px;text-align:center;color:var(--white);font-size:28px;font-weight:600}
.contact form{position:absolute;left:256px;top:160px;width:688px;height:412px;background:var(--white)}
.field{position:absolute;border:1px solid #bbb;font-size:12px;color:#555;padding:14px 14px;height:50px}
.submit{position:absolute;left:294px;top:316px;width:132px;height:50px;background:var(--sky);color:var(--white);font-family:"Montserrat",Arial,sans-serif;font-weight:600;font-size:16px;display:flex;align-items:center;justify-content:center}

/* footer */
.site-footer{top:5112px;height:213px;background:#2a8ee0;color:var(--white)}
.site-footer .brand{left:132px;top:60px;color:var(--white);font-size:34px}
.site-footer .brand small{font-size:16px;letter-spacing:9px}
.follow{left:490px;top:64px;font-size:12px;font-weight:700}
.footer-social{left:490px;top:108px}
.footer-social span{background:var(--white);color:var(--mid)}
.menu-title{left:720px;top:64px;font-size:12px;font-weight:700}
.menu{left:720px;top:98px;display:flex;gap:18px;font-size:10px}
.copy{left:720px;top:123px;font-size:10px;color:var(--mist)}
</style>
</head>
<body>

<header class="site-header">
  <div class="abs brand">BRIGHTVALE<small>imagery</small></div>
  <nav class="abs nav"><span>3D CAMERA</span><span>3D TOURS</span><span>SERVICES</span><span>BLOG</span><span>CONTACT US</span></nav>
  <div class="abs social header-social"><span aria-label="Quillnest">Q</span><span aria-label="Zembol">Z</span><span aria-label="Pondlarken">P</span></div>
</header>

<section class="hero" role="img" aria-label="Photograph of a large two-storey family home with a green front lawn under a blue sky">
  <svg class="abs play" width="110" height="110" viewBox="0 0 110 110"><circle cx="55" cy="55" r="50" fill="rgba(255,255,255,.25)" stroke="#fff" stroke-width="6"/><circle cx="55" cy="55" r="36" fill="#fff"/><polygon points="46,38 46,72 74,55" fill="#444"/></svg>
  <h1 class="abs">REAL ESTATE<br>VALUE PROPOSITION</h1>
  <div class="abs watch">WATCH NOW</div>
</section>

<section class="services">
  <div class="tile t1" role="img" aria-label="Blue-tinted photograph of a 3D scanning camera in a room"><h2>3D SCANS</h2><p>Capture every room in true depth with our scanning camera and share a precise model of your space online.</p></div>
  <div class="tile t2" role="img" aria-label="Blue-tinted photograph of a living room interior"><h2>VIRTUAL TOURS</h2><p>Let buyers walk through your property from any screen, any time, with smooth guided virtual tours.</p></div>
  <div class="tile t3" role="img" aria-label="Blue-tinted dollhouse model of a home"><h2>DOLLHOUSE</h2><p>See the whole building at once in a cutaway model that shows how every level and room connects.</p></div>
  <div class="tile t4" role="img" aria-label="Blue-tinted panoramic photograph of an interior"><h2>360 IMAGERY</h2><p>Full panoramic photos that let viewers look in every direction and feel the space as it really is.</p></div>
</section>

<section class="process">
  <h2 class="abs">HOW WE DO IT</h2>
  <div class="abs line"></div>
  <div class="step" style="left:263px"><h4>Scan</h4><div class="disc"><svg width="54" height="46" viewBox="0 0 54 46" fill="none" stroke="#2f90d8" stroke-width="3"><rect x="3" y="10" width="48" height="33" rx="4"/><path d="M17 10l4-7h12l4 7"/><circle cx="27" cy="26" r="10"/></svg></div><p>Capture a space<br>in <b>3D</b></p></div>
  <div class="step" style="left:593px"><h4>Upload</h4><div class="disc"><svg width="60" height="48" viewBox="0 0 60 48" fill="none" stroke="#2f90d8" stroke-width="3"><path d="M16 40H12a10 10 0 010-20 15 15 0 0129-4 11 11 0 017 24h-4"/><path d="M30 44V22M22 30l8-8 8 8"/></svg></div><p>Process &amp; store<br>in the <b>cloud</b></p></div>
  <div class="step" style="left:923px"><h4>View</h4><div class="disc"><svg width="34" height="58" viewBox="0 0 34 58" fill="none" stroke="#2f90d8" stroke-width="3"><rect x="3" y="3" width="28" height="52" rx="5"/><path d="M3 45h28M3 11h28"/><circle cx="17" cy="50" r="1.5"/></svg></div><p>Experience by<br><b>web &amp; mobile</b></p></div>
</section>

<section class="feature f1">
  <h2 class="abs" style="left:130px;top:122px">Buyers Love 360 degree Photos</h2>
  <svg class="abs" style="left:137px;top:238px" width="42" height="42" viewBox="0 0 42 42" fill="none" stroke="#3176b5" stroke-width="2.5"><path d="M2 2h38v38H2zM2 20h16V40M18 20V2"/></svg>
  <h3 class="abs" style="left:198px;top:234px;font-size:20px;font-weight:400">Live Floor Plan</h3>
  <p class="abs" style="left:198px;top:264px;font-size:10.5px;color:#333">Examine the floor from home</p>
  <div class="tablet" style="left:685px;top:71px;width:384px;height:291px"><div class="screen" role="img" aria-label="360 degree photo of a modern living room with a fireplace" style="background:linear-gradient(180deg,#e8e3da,#b9a68c)"></div></div>
</section>

<section class="feature f2">
  <div class="tablet" style="left:131px;top:65px;width:391px;height:291px"><div class="screen" role="img" aria-label="Video still of a 3D birds eye cutaway floor plan of an apartment" style="background:linear-gradient(160deg,#f2f2f2,#c8b8a8)"></div></div>
  <h2 class="abs" style="left:576px;top:101px;font-size:28px;line-height:44px">Detailed birds eye view with<br>our <em>Floor-plan</em> layouts</h2>
  <p class="abs" style="left:582px;top:190px;width:480px">Lorem Ipsum has been the industry's standard dummy text ever since the 1500s, when an unknown printer took a galley of type and scrambled it to make a type specimen book survived not only five centuries.</p>
  <span class="abs btn" style="left:577px;top:291px">Read More</span>
</section>

<section class="feature f3">
  <h2 class="abs" style="left:134px;top:102px">A 3D experience via our<br><em>Dollhouse</em> View</h2>
  <p class="abs" style="left:140px;top:210px;width:480px">Lorem Ipsum has been the industry's standard dummy text ever since the 1500s, when an unknown printer took a galley of type and scrambled it to make a type specimen book survived not only five centuries.</p>
  <span class="abs btn" style="left:136px;top:313px">Read More</span>
  <div class="tablet" style="left:682px;top:93px;width:387px;height:287px"><div class="screen" role="img" aria-label="Video still of a dollhouse cutaway model of a two-storey home" style="background:linear-gradient(160deg,#d9e6ef,#a47c5a)"></div></div>
</section>

<section class="benefits">
  <h2 class="abs">OUR BENEFITS</h2>
  <div class="abs line"></div>
  <div class="benefit" style="left:220px"><div class="disc"><svg width="44" height="50" viewBox="0 0 44 50" fill="none" stroke="#2f90d8" stroke-width="3"><path d="M14 26V6a4 4 0 018 0v14l12 3a5 5 0 014 6l-3 14H16L6 30a4 4 0 016-5z"/></svg></div><h4>HIGH CONVERSION</h4><p>On web pages with Brevolux content <b>67%</b> of users click through to the 3D virtual tour.</p></div>
  <div class="benefit" style="left:469px"><div class="disc"><svg width="50" height="50" viewBox="0 0 50 50" fill="none" stroke="#2f90d8" stroke-width="3"><circle cx="25" cy="25" r="21"/><path d="M25 12v13l9 6"/></svg></div><h4>GREATER ENGAGEMENT</h4><p>Buyers spend longer on pages with a 3D virtual tour, from 1:15 min <b>to 4:48 min.</b></p></div>
  <div class="benefit" style="left:731px"><div class="disc"><svg width="50" height="50" viewBox="0 0 50 50"><circle cx="25" cy="25" r="22" fill="#2f90d8"/><path d="M14 14c6 2 8 8 5 12s2 10 6 14M30 8c-2 6 6 8 4 14s6 6 10 4" stroke="#fff" stroke-width="3" fill="none"/></svg></div><h4>WORLDWIDE APPEAL</h4><p>A <b>75% increase</b> in international users, helping agents secure international investment.</p></div>
  <div class="benefit" style="left:998px"><div class="disc"><svg width="56" height="46" viewBox="0 0 56 46" fill="none" stroke="#2f90d8" stroke-width="3"><rect x="3" y="3" width="50" height="32" rx="2"/><path d="M20 44h16M28 35v9M10 27l12-10 8 6 14-12"/></svg></div><h4>BOOST TRAFFIC</h4><p>Listing with Brevolux content received a <b>49%</b> increase in web traffic and SEOs.</p></div>
</section>

<section class="freebies">
  <div class="abs photo" role="img" aria-label="Dollhouse cutaway render of a lit two-storey home at dusk"></div>
  <div class="abs panel">
    <h2>FREEBIES</h2>
    <ul>
      <li><svg width="34" height="30" viewBox="0 0 34 30" fill="none" stroke="#cee9f5" stroke-width="2"><rect x="2" y="2" width="30" height="26"/><path d="M2 9h30"/></svg>1.&nbsp; 3D Tour (Integrated into Nestboard &amp; homelistly.com.au)</li>
      <li><svg width="34" height="30" viewBox="0 0 34 30" fill="none" stroke="#cee9f5" stroke-width="2"><path d="M2 2h30v26H2zM2 15h14v13M16 15V2"/></svg>2.&nbsp; Traditional Floor and Site Plans (remove with measurements)</li>
      <li><svg width="34" height="30" viewBox="0 0 34 30" fill="none" stroke="#cee9f5" stroke-width="2"><rect x="6" y="2" width="22" height="26"/><path d="M11 9h12M11 15h12M11 21h12"/></svg>3.&nbsp; Company Branding &amp; Digital Presence</li>
      <li><svg width="34" height="30" viewBox="0 0 34 30" fill="none" stroke="#cee9f5" stroke-width="2"><rect x="2" y="2" width="30" height="20"/><path d="M12 28h10M17 22v6M8 16l6-6 5 4 7-7"/></svg>4.&nbsp; Fortnightly Analytic Reports</li>
      <li><svg width="34" height="30" viewBox="0 0 34 30" fill="none" stroke="#cee9f5" stroke-width="2"><rect x="2" y="2" width="30" height="26"/><path d="M2 9h30M8 16h8M8 21h14"/></svg>5.&nbsp; Leading Web Integration and Backend Support</li>
    </ul>
  </div>
</section>

<section class="feed">
  <h2 class="abs">QUILLNEST FEED</h2>
  <svg class="abs" style="left:84px;top:172px" width="14" height="22" viewBox="0 0 14 22" fill="none" stroke="#999" stroke-width="2.5"><path d="M12 2L3 11l9 9"/></svg>
  <svg class="abs" style="left:1118px;top:172px" width="14" height="22" viewBox="0 0 14 22" fill="none" stroke="#999" stroke-width="2.5"><path d="M2 2l9 9-9 9"/></svg>
  <div class="post" style="left:136px"><div class="thumb" role="img" aria-label="Small photo of a room"></div><div><h4>Contrary to popular belief, Lorem Ipsum is not simply random text.</h4><p>17 people recommended this</p></div></div>
  <div class="divider" style="left:434px"></div>
  <div class="post" style="left:480px"><div class="thumb" role="img" aria-label="Small photo of a home"></div><div><h4>It is a long established fact that a reader will be distracted by</h4><p>5 people recommended this</p></div></div>
  <div class="divider" style="left:790px"></div>
  <div class="post" style="left:836px"><div class="thumb" role="img" aria-label="Small photo of an interior"></div><div><h4>There are many variations of passages of Lorem Ipsum.</h4><p>5 people recommended this</p></div></div>
</section>

<section class="contact">
  <h2 class="abs">GET IN TOUCH</h2>
  <form>
    <div class="field" style="left:46px;top:51px;width:284px">Name</div>
    <div class="field" style="left:46px;top:126px;width:284px">E-mail</div>
    <div class="field" style="left:46px;top:203px;width:284px">Phone</div>
    <div class="field" style="left:362px;top:26px;width:280px;height:213px">Message</div>
    <div class="submit">SUBMIT</div>
  </form>
</section>

<footer class="site-footer">
  <div class="abs brand">BRIGHTVALE<small>imagery</small></div>
  <div class="abs follow">FOLLOW US</div>
  <div class="abs social footer-social"><span aria-label="Quillnest">Q</span><span aria-label="Zembol">Z</span><span aria-label="Pondlarken">P</span></div>
  <div class="abs menu-title">MENU</div>
  <div class="abs menu"><span>3D CAMERA</span><span>3D TOURS</span><span>SERVICES</span><span>BLOG</span><span>CONTACT US</span></div>
  <div class="abs copy">Copyright © 2017 Brightvale. All Rights Reserved.</div>
</footer>

</body>
</html>
```